Jolly Paws Business Card Update

I have a business card which I love. I want to keep the same logo, colours, font and style. I want to upgrade the scripting and remove some elements and add others.
On the front side under Services - remove the existing wording and insert - Providing individual coaching strategies to create happy, healthy and social canine companions
Under Rebecca Thornley amend the current wording to read: Qualified in Dog Behavioural Training, Natural Animal Healthcare and Animal Health Science
On the reverse side to remove the web address.

```html
<!DOCTYPE html>
<html lang="en">
<head>
<meta charset="utf-8">
<title>Jolly Paws Business Card</title>
<link href="https://fonts.googleapis.com/css2?family=Arimo:wght@400;700&display=swap" rel="stylesheet">
<style>
  :root {
    --page-bg: #d9d4cc;
    --blue-light: #1a9ad8;
    --blue-dark: #1d55a8;
    --cream: #f4ecd2;
    --cream-light: #fbf6e4;
    --red-bright: #e8202a;
    --red-dark: #7d0f13;
    --ink: #111111;
    --white: #ffffff;
  }
  * { margin: 0; padding: 0; box-sizing: border-box; }
  html, body { width: 900px; height: 1200px; overflow: hidden; }
  body {
    background: var(--page-bg);
    font-family: "Arimo", Arial, sans-serif;
    position: relative;
  }
  .card {
    position: absolute;
    left: 73px;
    width: 777px;
    border-radius: 22px;
    overflow: hidden;
  }
  /* Front */
  .card-front { top: 130px; height: 452px; }
  .front-top {
    position: absolute; left: 0; top: 0; width: 100%; height: 222px;
    background: linear-gradient(180deg, var(--blue-light) 0%, #1679c8 100%);
  }
  .brand-mark {
    position: absolute; left: 99px; top: 38px; width: 160px; height: 160px;
    border-radius: 50%;
    background: var(--cream);
    border: 12px solid var(--red-bright);
    display: flex; align-items: center; justify-content: center;
  }
  .brand-mark-name {
    color: var(--red-dark); font-size: 20px; font-weight: 700; text-align: center; line-height: 1.15;
  }
  .front-divider {
    position: absolute; left: 279px; top: 45px; width: 2px; height: 148px; background: var(--cream);
  }
  .services-title {
    position: absolute; left: 309px; top: 42px;
    color: var(--cream); font-size: 21px; letter-spacing: 0.5px;
  }
  .services-list {
    position: absolute; left: 309px; top: 80px;
    color: var(--white); font-size: 18px; line-height: 25.5px;
  }
  .mission-band {
    position: absolute; left: 0; top: 222px; width: 100%; height: 56px;
    background: linear-gradient(90deg, var(--cream) 0%, var(--cream-light) 50%, var(--cream) 100%);
    display: flex; align-items: center; justify-content: center;
    text-align: center; color: var(--ink); font-size: 18px; line-height: 23px;
    padding-left: 40px;
  }
  .front-bottom {
    position: absolute; left: 0; top: 278px; width: 100%; height: 174px;
    background: linear-gradient(90deg, var(--red-dark) 0%, var(--red-bright) 48%, var(--red-dark) 100%);
  }
  .contact-name {
    position: absolute; right: 358px; top: 30px;
    color: var(--white); font-size: 26px;
  }
  .qualifications {
    position: absolute; right: 358px; top: 70px;
    color: var(--white); font-size: 18px; line-height: 25px; text-align: right;
  }
  .contact-divider {
    position: absolute; left: 428px; top: 70px; width: 2px; height: 74px; background: var(--cream);
  }
  .contact-list {
    position: absolute; left: 440px; top: 76px; list-style: none;
    color: var(--white); font-size: 21px; line-height: 30px;
  }
  .contact-list li { display: flex; align-items: center; gap: 8px; }
  .contact-list svg { width: 22px; height: 22px; flex: none; }
  /* Back */
  .card-back {
    top: 618px; height: 459px;
    background: linear-gradient(180deg, var(--blue-light) 0%, var(--blue-dark) 100%);
  }
  .back-mark {
    position: absolute; left: 299px; top: 63px; width: 180px; height: 180px;
    border-radius: 50%; background: var(--cream); border: 14px solid var(--red-bright);
  }
  .back-name {
    position: absolute; left: 0; top: 258px; width: 100%; text-align: center;
    color: var(--cream); font-size: 46px; font-weight: 700; letter-spacing: 2px;
  }
  .tagline {
    position: absolute; left: 0; top: 315px; width: 100%; text-align: center;
    color: var(--white); font-size: 22px; letter-spacing: 0.3px;
  }
  .back-wave { position: absolute; left: 0; bottom: 0; width: 777px; height: 80px; }
</style>
</head>
<body>
  <section class="card card-front">
    <div class="front-top">
      <div class="brand-mark"><span class="brand-mark-name">Jolly<br>Paws</span></div>
      <div class="front-divider"></div>
      <h2 class="services-title">SERVICES</h2>
      <p class="services-list">Behaviour Consults, Training,<br>Complex Skills and Walking Coaching,<br>Diet &amp; Nutrition, Massage,<br>Natural Healthcare Options</p>
    </div>
    <p class="mission-band">Providing individual coaching strategies to create happy, healthy and<br>social canine companions</p>
    <div class="front-bottom">
      <h1 class="contact-name">Rebecca Thornley</h1>
      <p class="qualifications">Qualified in Dog Behavioural<br>Training, Natural Animal Healthcare and<br>Animal Health Science</p>
      <div class="contact-divider"></div>
      <ul class="contact-list">
        <li>
          <svg viewBox="0 0 22 22"><circle cx="11" cy="11" r="10" fill="#f4ecd2"/><rect x="7.5" y="5" width="7" height="12" rx="1.5" fill="#9e1418"/><rect x="8.8" y="6.5" width="4.4" height="6" fill="#f4ecd2"/></svg>
          0400 275 618
        </li>
        <li>
          <svg viewBox="0 0 22 22"><circle cx="11" cy="11" r="10" fill="#f4ecd2"/><rect x="5.5" y="7" width="11" height="8" rx="1" fill="#9e1418"/><path d="M5.8 7.4 11 11.6l5.2-4.2" fill="none" stroke="#f4ecd2" stroke-width="1.2"/></svg>
          jollypaws1@mailbox.com
        </li>
      </ul>
    </div>
  </section>

  <section class="card card-back">
    <div class="back-mark"></div>
    <h2 class="back-name">JOLLY PAWS</h2>
    <p class="tagline">HAPPY DOGS, HAPPY OWNERS</p>
    <svg class="back-wave" viewBox="0 0 777 80" preserveAspectRatio="none">
      <defs>
        <linearGradient id="waveRed" x1="0" x2="1" y1="0" y2="0">
          <stop offset="0" stop-color="#7d0f13"/>
          <stop offset="0.48" stop-color="#e8202a"/>
          <stop offset="1" stop-color="#7d0f13"/>
        </linearGradient>
      </defs>
      <path d="M0 40 Q388 -18 777 40 L777 80 L0 80 Z" fill="#f4ecd2"/>
      <path d="M0 46 Q388 -10 777 46 L777 80 L0 80 Z" fill="url(#waveRed)"/>
    </svg>
  </section>
</body>
</html>
```